Website for Sports and Exercise Medicine Doctor with active research in stem cells therapies.

I am a sports and exercise medicine doctor with research interests in the cutting edge areas of biological therapies, most notable stem cells. None of my patients are dying of anything, and most of them come to see me to decrease their pain, so they can get back to what they want to do.

The approach i then take is to decrease their pain and support them to achieve the things they wish to achieve. Most people start at "Just make it stop hurting doc" , but I try to move them towards something more important over time.

I would like the website to be very different to other "Doctor or medical websites" in its look. No pictures of doctors in white coats and no pictures of fit old people smiling. I would potentially like the fist thing seen to be a quote:

"Less pain. Everybody wants it, but what are you going to do, once you've got it?"

(But this is only an idea, I am open to anything)

The website will need a couple of things

1. "Locations" I work
2. "Research" I am involved in
3. "Sort Me out" - Clinical information for people to access
4. "Social" - imbedded twitter and facebook
5. "Blog" - imbedded wordpress blog
6. "Bio" - the usual bio-stuff

The "Sort Me out" - pages I would like to have the functionality as seen in this site http://www.veltarion.com.au/platelet/. I intend to put disease topics into these pages (eg Achilles tehdinopathy, osteoarthritis etc etc etc). Once again I am not wedded to this but something along these lines would be good.

To give you an idea these are some sites I like
http://www.morbanquilt.com/
http://daptrine.com/
http://ovimbera.com.sg/
http://jolvaniketchup.com/
http://www.pilnorwave.com/
http://quadrisel.com/#offering
http://fennikstudio.tv/
http://norvalgate.com/
http://sablethorn.co.uk/#about

Target Market(s)

20-80 year old.
People with tendon injuries
People with osteoarthritis
People interested in stem cells
I will build the site over time to contain information on multiple sporting injuries and musculoskeletal disorders. It will also become a site for the latest on stem cell research particularly in the area of osteoarthritis.

Industry/Entity Type

Medical

Font styles to use
Sans Serif

Colors
ffffff

Requirements
Nice to have
• To give you an idea these are some sites I like
http://daptrine.com/
http://fennikstudio.tv/
http://norvalgate.com/
Should not have
• Pictures of doctors in white coats or old fit people smiling

```html
<!DOCTYPE html>
<html lang="en">
<head>
<meta charset="utf-8">
<title>Dr Rob Calder</title>
<link rel="stylesheet" href="https://fonts.googleapis.com/css2?family=Arimo:wght@400;700&display=swap">
<style>
:root{
  --green:#7cc242;
  --teal:#0b6457;
  --ink:#1e2a2f;
  --body:#555;
  --muted:#777;
  --panel:#f4f4f4;
  --foot:#232526;
}
*{box-sizing:border-box;margin:0;padding:0}
html,body{width:909px;height:1200px;overflow:hidden;background:#fff}
body{position:relative;font-family:"Arimo",Arial,sans-serif;color:var(--ink)}
.abs{position:absolute}
.topbar{left:0;top:0;width:909px;height:4px;background:var(--green)}
.brand{left:152px;top:46px;display:flex;align-items:center;gap:7px}
.brand-dot{width:30px;height:30px;border-radius:50%;background:var(--green)}
.brand-name{font-size:20px;color:var(--teal);font-weight:400}
.call{left:456px;top:28px;display:flex;align-items:center;gap:6px;font-size:11px;color:var(--teal)}
.call b{font-weight:400;color:var(--green)}
.search{left:609px;top:22px;width:149px;height:26px;border:1px solid #e2e2e2;box-shadow:0 1px 2px rgba(0,0,0,.08)}
.search span{position:absolute;left:12px;top:8px;font-size:6px;color:#bbb}
.search svg{position:absolute;right:9px;top:7px}
.nav a{position:absolute;top:75px;font-size:7px;color:var(--teal);text-decoration:none}
.nav-active{left:385px;top:101px;width:31px;height:3px;background:var(--green)}
.hero{left:0;top:104px;width:909px;height:294px;background:radial-gradient(ellipse at 65% 45%,#1b8c9c 0%,#0c4d5a 30%,#072b33 60%,#041a1f 100%)}
.hero-title{left:152px;top:188px;font-size:18px;line-height:22px;color:var(--green);font-weight:400}
.hero-text{left:152px;top:246px;width:185px;font-size:10.5px;line-height:14.5px;color:#fff}
.btn-green{left:152px;top:314px;width:73px;height:28px;background:var(--green);color:#fff;font-size:11px;display:flex;align-items:center;justify-content:center}
.arrow{top:216px;width:22px;height:48px;background:var(--green);display:flex;align-items:center;justify-content:center}
.dot{top:380px;width:8px;height:8px;border-radius:50%;background:#fff}
.h2{font-size:14.5px;font-weight:400;color:var(--ink)}
.welcome-text{left:152px;top:446px;width:370px;font-size:6.8px;line-height:10.9px;color:var(--body)}
.btn-teal{left:151px;top:520px;width:63px;height:28px;background:var(--teal);color:#fff;font-size:11px;display:flex;align-items:center;justify-content:center;box-shadow:0 1px 2px rgba(0,0,0,.3)}
.bio{left:554px;top:406px;width:203px;height:153px;background:var(--teal);border:2px solid #e6e6e6;box-shadow:0 1px 3px rgba(0,0,0,.2)}
.bio-photo{left:0;top:0;width:124px;height:149px;background:linear-gradient(180deg,#3c7d78,#d8dde0 70%,#f1f3f4)}
.bio-label{left:115px;top:56px;font-size:29px;color:#fff}
.research{left:0;top:570px;width:909px;height:256px;background:var(--panel)}
.card{top:612px;width:188px;height:196px;background:#fff;border-top:4px solid var(--green);box-shadow:0 2px 4px rgba(0,0,0,.12)}
.card-photo{left:1px;top:0;width:186px;height:100px}
.card-title{left:7px;top:112px;font-size:10.5px;color:var(--teal)}
.card-text{left:8px;top:131px;width:172px;font-size:6.6px;line-height:10.8px;color:var(--body)}
.card-link{left:8px;top:170px;font-size:6.8px;color:var(--ink)}
.date{width:34px;height:88px}
.date-icon{left:0;top:0;width:34px;height:28px;border:1px solid #e3e3e3;display:flex;align-items:center;justify-content:center}
.date-day{left:0;top:28px;width:34px;height:38px;border:1px solid #e3e3e3;border-top:0;text-align:center;color:#999;font-size:7px;padding-top:6px;line-height:11px}
.date-day b{display:block;font-weight:400;font-size:10px}
.date-count{left:0;top:66px;width:34px;height:20px;background:var(--green);color:#fff;font-size:7px;display:flex;align-items:center;justify-content:center;gap:2px}
.post-photo{width:148px;height:70px}
.post-title{font-size:10.5px;font-weight:700;color:var(--ink)}
.post-meta{font-size:6.5px;color:var(--green);display:flex;gap:6px;align-items:center}
.post-text{width:150px;font-size:7.4px;line-height:13.6px;color:var(--muted)}
.rule{height:4px;background:#efefef}
.btn-line{width:64px;height:23px;border:2px solid var(--green);color:var(--teal);font-size:7px;display:flex;align-items:center;justify-content:center;background:#fff}
.footer{left:0;top:1104px;width:909px;height:96px;background:var(--foot);border-top:5px solid var(--green)}
.foot-links{left:152px;top:26px;font-size:7px;color:#fff}
.foot-copy{left:152px;top:47px;font-size:7px;color:#fff}
.social{top:35px;width:22px;height:22px;border-radius:50%;background:#e9e9e9;border:2px solid #888}
</style>
</head>
<body>
<div class="abs topbar"></div>

<header>
  <div class="abs brand"><span class="brand-dot"></span><span class="brand-name">Dr RobCalder</span></div>
  <div class="abs call">
    <svg width="22" height="16" viewBox="0 0 22 16"><path d="M2 6c3-5 15-5 18 0l-3 2-2-3H7L5 8z" fill="#1d5fa8"/><rect x="5" y="8" width="12" height="7" rx="2" fill="#1d5fa8"/><circle cx="11" cy="11.5" r="2" fill="#fff"/></svg>
    <span>Call us : <b>123 456 789</b></span>
  </div>
  <div class="abs search"><span>Search</span>
    <svg width="11" height="11" viewBox="0 0 11 11"><circle cx="4.5" cy="4.5" r="3.5" fill="none" stroke="#111" stroke-width="1.5"/><path d="M7 7l3 3" stroke="#111" stroke-width="1.6"/></svg>
  </div>
  <nav class="nav">
    <a style="left:390px">Home</a><a style="left:439px">Location</a><a style="left:497px">Research</a><a style="left:558px">Sort me</a><a style="left:614px">Out Socail</a><a style="left:678px">Blog</a><a style="left:723px">Bio</a>
  </nav>
  <div class="abs nav-active"></div>
</header>

<section class="abs hero" role="img" aria-label="Glowing blue DNA double helix on a dark background">
</section>
<h1 class="abs hero-title">Nulla convallis egestas<br>Lorem ipsum dolor</h1>
<p class="abs hero-text">Lorem ipsum dolor sit amet, consec-tetur adipiscing elit. Nulla convallis egestas Lorem ipsum dolor sit amet, consectetur adipiscing elit. Nulla</p>
<div class="abs btn-green">More..</div>
<div class="abs arrow" style="left:0"><svg width="10" height="14" viewBox="0 0 10 14"><path d="M8 1L2 7l6 6" fill="none" stroke="#fff" stroke-width="3"/></svg></div>
<div class="abs arrow" style="left:887px"><svg width="10" height="14" viewBox="0 0 10 14"><path d="M2 1l6 6-6 6" fill="none" stroke="#fff" stroke-width="3"/></svg></div>
<div class="abs dot" style="left:452px;background:var(--green);border:1px solid #fff"></div>
<div class="abs dot" style="left:465px"></div>
<div class="abs dot" style="left:478px"></div>

<section>
  <h2 class="abs h2" style="left:152px;top:423px">Welcome To <span style="color:var(--teal)">Rob Calder</span></h2>
  <p class="abs welcome-text">Lorem ipsum dolor sit amet, consectetur adipiscing elit. Nulla convallis egestas rhoncus. Donec facilisis fermentum sem, ac viverra ante luctus vel. Donec vel mauris quam. Aliquam pellentesque pellentesque turpis, ut bibendum sapien sollicitudin nec. Pellentesque posuere ornare placerat. Suspendisse potenti. Quisque massa tortor, tristique non tristique at, luctus sed massa. Donec libero eros, mollis ac...Lorem ipsum dolor sit amet, consectetur adipiscing elit. Nulla convallis egestas rhoncus. Donec facilisis fermentum sem, ac viverra ante luctus vel. Donec vel mauris quam.</p>
  <div class="abs btn-teal">More..</div>
  <div class="abs bio">
    <div class="abs bio-photo" role="img" aria-label="Portrait photo for the biography"></div>
    <div class="abs bio-label">Bio</div>
  </div>
</section>

<section class="abs research"></section>
<h2 class="abs h2" style="left:152px;top:581px">Research</h2>
<article class="abs card" style="left:151px">
  <div class="abs card-photo" role="img" aria-label="Laboratory photo with sample bottles" style="background:linear-gradient(135deg,#c9cfd4,#8e9aa4 60%,#d7dadc)"></div>
  <h3 class="abs card-title" style="font-weight:400">Research</h3>
  <p class="abs card-text">Lorem ipsum dolor sit amet, consectetur adipiscing elit. Nulla convallis egestas rhoncus. Donec facilisis fermetupotenti. .</p>
  <span class="abs card-link">Read more</span>
</article>
<article class="abs card" style="left:362px">
  <div class="abs card-photo" role="img" aria-label="Laboratory photo with a microscope" style="background:linear-gradient(135deg,#3b2d26,#7b6a5c 50%,#e2e2e2)"></div>
  <h3 class="abs card-title" style="font-weight:400">Bio Research</h3>
  <p class="abs card-text">Lorem ipsum dolor sit amet, consectetur adipiscing elit. Nulla convallis egestas rhoncus. Donec facilisis fermetupotenti. .</p>
  <span class="abs card-link">Read more</span>
</article>
<article class="abs card" style="left:568px">
  <div class="abs card-photo" role="img" aria-label="Chemistry photo with a glass flask" style="background:linear-gradient(135deg,#eef2f2,#b9c2c1 50%,#4e7a3a)"></div>
  <h3 class="abs card-title" style="font-weight:400">Chemical</h3>
  <p class="abs card-text">Lorem ipsum dolor sit amet, consectetur adipiscing elit. Nulla convallis egestas rhoncus. Donec facilisis fermetupotenti. .</p>
  <span class="abs card-link">Read more</span>
</article>

<h2 class="abs h2" style="left:152px;top:842px">Blog</h2>

<!-- post 1 -->
<div class="abs date" style="left:152px;top:872px">
  <div class="abs date-icon"><svg width="12" height="14" viewBox="0 0 12 14"><path d="M1 0h7l4 4v10H1z" fill="#7cc242"/><path d="M3 7h6M3 9.5h6" stroke="#fff"/></svg></div>
  <div class="abs date-day">Nov 20<b>2013</b></div>
  <div class="abs date-count">&#9679; 0</div>
</div>
<div class="abs post-photo" style="left:197px;top:872px;background:linear-gradient(135deg,#e8eef2,#b8c7d3 55%,#5e86b3)" role="img" aria-label="Blog photo of a clinic visit"></div>
<h3 class="abs post-title" style="left:197px;top:958px">Mvelit ac diam tincidu</h3>
<div class="abs post-meta" style="left:197px;top:977px"><span style="color:#888">&#9679;</span><span style="color:#888">&#9670;</span></div>
<p class="abs post-text" style="left:197px;top:997px">Proin lobortis tempus odio eget venenatis. Proin fermentum ut massa at bibendum. Proin bibendum...</p>
<div class="abs rule" style="left:152px;top:1062px;width:130px"></div>
<div class="abs btn-line" style="left:281px;top:1053px">Read More..</div>

<!-- post 2 -->
<div class="abs date" style="left:357px;top:872px">
  <div class="abs date-icon"><svg width="14" height="12" viewBox="0 0 14 12"><path d="M0 3h4l1-2h4l1 2h4v9H0z" fill="#7cc242"/><circle cx="7" cy="7" r="2.5" fill="none" stroke="#fff" stroke-width="1.3"/></svg></div>
  <div class="abs date-day">Nov 20<b>2013</b></div>
  <div class="abs date-count">&#9679; 0</div>
</div>
<div class="abs post-photo" style="left:402px;top:872px;background:linear-gradient(135deg,#f1f1f1,#c9c3b9 55%,#8796a6)" role="img" aria-label="Blog photo of a consultation"></div>
<h3 class="abs post-title" style="left:402px;top:958px">Chronic Exposure to Noise</h3>
<div class="abs post-meta" style="left:402px;top:977px"><span style="color:#888">&#9679;</span><span style="color:#888">&#9670;</span><span>tovelin</span></div>
<p class="abs post-text" style="left:402px;top:997px">Proin lobortis tempus odio eget venenatis. Proin fermentum ut massa at bibendum. Proin bibendum...</p>
<div class="abs rule" style="left:357px;top:1062px;width:130px"></div>
<div class="abs btn-line" style="left:486px;top:1053px">Read More..</div>

<!-- post 3 -->
<div class="abs date" style="left:563px;top:872px">
  <div class="abs date-icon"><svg width="14" height="14" viewBox="0 0 14 14"><rect x="1" y="1" width="6" height="6" rx="3" fill="none" stroke="#7cc242" stroke-width="2"/><rect x="7" y="7" width="6" height="6" rx="3" fill="none" stroke="#7cc242" stroke-width="2"/><path d="M5 5l4 4" stroke="#7cc242" stroke-width="2"/></svg></div>
  <div class="abs date-day">Nov 20<b>2013</b></div>
  <div class="abs date-count">&#9679; 0</div>
</div>
<div class="abs post-photo" style="left:608px;top:872px;background:linear-gradient(90deg,#f2f3f4,#d9dcdf 55%,#b4bcc4)" role="img" aria-label="Blog photo of a practitioner"></div>
<h3 class="abs post-title" style="left:608px;top:958px">Nulla vitae elit nec purus</h3>
<div class="abs post-meta" style="left:608px;top:977px"><span>&#9679; tov</span><span>&#9670; tovelin</span></div>
<p class="abs post-text" style="left:608px;top:997px">Proin lobortis tempus odio eget venenatis. Proin fermentum ut massa at bibendum. Proin bibendum...</p>
<div class="abs rule" style="left:563px;top:1062px;width:130px"></div>
<div class="abs btn-line" style="left:692px;top:1053px">Read More..</div>

<footer class="abs footer">
  <div class="abs foot-links">Home &nbsp;|&nbsp; About us &nbsp;|&nbsp; Counselling &nbsp;|&nbsp; Workshop &nbsp;|&nbsp; Contact us</div>
  <div class="abs foot-copy">Content copyright 2013. DR Robcalder. All rights reserved.</div>
  <div class="abs social" style="left:679px"></div>
  <div class="abs social" style="left:706px"></div>
  <div class="abs social" style="left:733px"></div>
</footer>
</body>
</html>
```